Business Card

Please design a business card with our logo on a cream coloured background and include the following information:

Tallowmere Shopping Centre
ph (08) 9314 8806

sales@quillmeadowflorist.com

www.quillmeadowflorist.com

on reverse:

Find us on Facebook
facebook.com/quillmeadowflorist

```html
<!DOCTYPE html>
<html lang="en">
<head>
<meta charset="utf-8">
<title>Quill Meadow Florist – Business Card</title>
<link href="https://fonts.googleapis.com/css2?family=Ubuntu+Condensed&family=Open+Sans:wght@400;600&display=swap" rel="stylesheet">
<style>
  :root {
    --green: #3f7f26;
    --green-light: #55952f;
    --green-dark: #2f6a1c;
    --charcoal: #3a3b3d;
    --ink: #333436;
    --grey: #6b6d70;
    --paper: #ffffff;
    --backdrop: #ecebe6;
  }
  * { box-sizing: border-box; margin: 0; padding: 0; }
  html, body {
    width: 1200px; height: 1024px; overflow: hidden;
    background: var(--backdrop);
  }
  .sheet { position: relative; width: 1200px; height: 1024px; }
  .card {
    position: absolute; left: 250px; width: 700px; height: 400px;
    overflow: hidden; border-radius: 3px;
    box-shadow: 0 6px 18px rgba(0,0,0,.18);
  }
  .card--front { top: 80px; background: var(--paper); }
  .card--back {
    top: 544px;
    background: radial-gradient(ellipse at 45% 40%, var(--green-light), var(--green-dark) 85%);
  }

  /* Front */
  .front-swoosh { position: absolute; inset: 0; }
  .brand {
    position: absolute; left: 50px; top: 60px; width: 320px;
    display: flex; flex-direction: column; align-items: center; gap: 10px;
  }
  .brand-dot {
    width: 52px; height: 52px; border-radius: 50%;
    border: 3px solid var(--green);
  }
  .brand-name {
    font-family: "Ubuntu Condensed", sans-serif;
    font-size: 34px; line-height: 1.1; color: var(--ink);
    white-space: nowrap;
  }
  .location {
    position: absolute; left: 50px; top: 186px; width: 320px; text-align: center;
    font-family: "Open Sans", sans-serif;
  }
  .location-centre { font-size: 16px; font-weight: 600; color: var(--green); }
  .location-social { font-size: 14px; color: var(--grey); margin-top: 2px; }
  .divider {
    position: absolute; left: 398px; top: 110px; width: 2px; height: 90px;
    background: linear-gradient(var(--grey), transparent);
  }
  .contact {
    position: absolute; left: 418px; top: 116px;
    font-family: "Open Sans", sans-serif; font-size: 13px; color: var(--grey);
    list-style: none; white-space: nowrap;
  }
  .contact li { display: flex; align-items: center; gap: 8px; margin-bottom: 12px; }
  .contact svg { width: 13px; height: 13px; flex: none; }
  .front-web {
    position: absolute; left: 40px; bottom: 22px;
    font-family: "Open Sans", sans-serif; font-size: 13px; color: var(--paper);
  }

  /* Back */
  .back-brand {
    position: absolute; left: 0; right: 0; top: 130px;
    display: flex; align-items: center; justify-content: center; gap: 18px;
  }
  .back-dot {
    width: 64px; height: 64px; border-radius: 50%;
    border: 4px solid var(--paper); flex: none;
  }
  .back-name {
    font-family: "Ubuntu Condensed", sans-serif;
    font-size: 48px; color: var(--paper); white-space: nowrap;
  }
  .back-web {
    position: absolute; left: 0; right: 0; top: 240px; text-align: center;
    font-family: "Open Sans", sans-serif; font-size: 14px; color: var(--paper);
  }
</style>
</head>
<body>
<main class="sheet">
  <section class="card card--front">
    <svg class="front-swoosh" viewBox="0 0 700 400" preserveAspectRatio="none" aria-hidden="true">
      <path d="M0 350 C 260 345, 540 300, 700 175 L700 215 C 540 330, 270 362, 0 364 Z" fill="var(--charcoal)"/>
      <path d="M0 366 C 270 364, 540 335, 700 220 L700 400 L0 400 Z" fill="var(--green)"/>
    </svg>
    <div class="brand">
      <span class="brand-dot"></span>
      <span class="brand-name">Quill Meadow Florist</span>
    </div>
    <div class="location">
      <p class="location-centre">Tallowmere Shopping Centre</p>
      <p class="location-social">facebook.com/quillmeadowflorist</p>
    </div>
    <span class="divider"></span>
    <ul class="contact">
      <li>
        <svg viewBox="0 0 14 14" aria-hidden="true"><rect x="1" y="1" width="12" height="12" rx="2" fill="var(--green)"/><path d="M4 7 l2 2 l4 -4" stroke="#fff" stroke-width="1.6" fill="none"/></svg>
        (08) 9314 8806
      </li>
      <li>
        <svg viewBox="0 0 14 14" aria-hidden="true"><rect x="1.5" y="1.5" width="11" height="11" rx="2" fill="none" stroke="var(--grey)" stroke-width="1.4"/></svg>
        sales@quillmeadowflorist.com
      </li>
    </ul>
    <p class="front-web">www.quillmeadowflorist.com</p>
  </section>

  <section class="card card--back">
    <div class="back-brand">
      <span class="back-dot"></span>
      <span class="back-name">Quill Meadow Florist</span>
    </div>
    <p class="back-web">www.quillmeadowflorist.com</p>
  </section>
</main>
</body>
</html>
```